QM active wear

Hey There

QM is a brand new active wear Sydney base company. our clothe design by professional dancers & athletics. pushing the niche market of active wear. the products we have is cool fashionable functional Eco friendly!!!

it caters male and female. who stays active and wants to be chic at the same time.
we would like to be associate with K-8 & Coastal garments & Vorn kind of brands.

i need you guys to use the existing logo to restructure it. turn it into consistent format that can be shared through out all the electronic business stationery. pls refer to all the photos i have upload in this brief. hopefully it'll gives you guys more of what i like i needs to be done.

PS: business card material specifications needs to be provided.
just so send the details to the printing company without explain too much.

Cheers

Industry/Entity Type

Electronic

Requirements
Must have
• It needs be more readable. clean. current. pop. fashionable.
interesting details across the broad for all electronic stationary.

for you to think about it and working on : company's business letters, order forms, its notices and other official publications, promissory notes, endorsements, cheques and orders for money or goods purporting to be signed by, or on behalf of, the company invoices, receipts websites

```html
<!DOCTYPE html>
<html lang="en">
<head>
<meta charset="utf-8">
<title>QM active wear — business card</title>
<link href="https://fonts.googleapis.com/css2?family=Roboto:wght@300;400;500&display=swap" rel="stylesheet">
<style>
  :root {
    --backdrop: #e9e9ea;
    --card: #f7f7f7;
    --ink: #222222;
    --ink-soft: #444444;
    --mark: #000000;
    --mark-text: #ffffff;
    --rule: #555555;
    --red: #d0413a;
    --orange: #e6a63c;
    --yellow: #ece676;
    --green: #77b466;
    --blue: #4d7fcc;
    --violet: #5a52c0;
    --plum: #8a1f63;
  }
  * { margin: 0; padding: 0; box-sizing: border-box; }
  html, body {
    width: 1200px; height: 720px; overflow: hidden;
    background: var(--backdrop);
    font-family: "Roboto", Arial, sans-serif;
    color: var(--ink);
  }
  .stage {
    width: 1200px; height: 720px;
    display: flex; align-items: center; justify-content: center; gap: 50px;
  }
  .card {
    position: relative;
    width: 540px; height: 310px;
    background: var(--card);
    overflow: hidden;
    box-shadow: 0 2px 6px rgba(0,0,0,.12);
  }
  .pattern-band {
    position: absolute; left: 0; width: 100%;
    background: linear-gradient(90deg, var(--yellow), var(--orange), var(--red), var(--plum), var(--violet), var(--blue), var(--green), var(--yellow), var(--orange), var(--red), var(--plum), var(--blue));
  }
  .pattern-band--top {
    top: 0; height: 70px;
    clip-path: polygon(0 0, 60% 0, 56% 60%, 48% 100%, 40% 70%, 32% 100%, 24% 70%, 16% 100%, 8% 70%, 0 100%);
  }
  .pattern-band--bottom {
    bottom: 0; height: 90px;
    clip-path: polygon(30% 100%, 34% 40%, 44% 75%, 52% 30%, 62% 65%, 72% 20%, 82% 55%, 92% 10%, 100% 0, 100% 100%);
  }
  .identity {
    position: absolute; left: 36px; top: 112px;
  }
  .identity__name {
    font-size: 34px; font-weight: 400; letter-spacing: 1px; line-height: 1;
  }
  .identity__title {
    margin-top: 6px; font-size: 15px; font-weight: 400; color: var(--ink-soft);
  }
  .contact { margin-top: 14px; list-style: none; }
  .contact__item {
    display: flex; align-items: center; gap: 10px;
    font-size: 15px; font-weight: 300; color: var(--ink-soft);
    margin-top: 6px;
  }
  .contact__icon { width: 18px; height: 14px; flex: none; }
  .divider {
    position: absolute; left: 300px; top: 40px;
    width: 1px; height: 150px; background: var(--rule);
  }
  .brand-mark {
    position: absolute; display: flex; align-items: center; justify-content: center;
    border-radius: 50%; background: var(--mark);
    color: var(--mark-text); font-weight: 500; letter-spacing: 2px;
  }
  .brand-mark--front { left: 345px; top: 40px; width: 118px; height: 118px; font-size: 38px; }
  .brand-mark--back { left: 195px; top: 80px; width: 150px; height: 150px; font-size: 48px; }
  .pattern-field {
    position: absolute; inset: 0;
    background: linear-gradient(135deg, var(--green), var(--yellow) 15%, var(--orange) 28%, var(--red) 40%, var(--plum) 52%, var(--violet) 64%, var(--blue) 76%, var(--green) 88%, var(--yellow));
  }
</style>
</head>
<body>
<main class="stage">
  <section class="card card--front" aria-label="Business card front">
    <div class="pattern-band pattern-band--top" role="img" aria-label="Multicolour zigzag chevron pattern"></div>
    <div class="pattern-band pattern-band--bottom" role="img" aria-label="Multicolour zigzag chevron pattern"></div>
    <div class="identity">
      <h1 class="identity__name">QM</h1>
      <p class="identity__title">Business Title</p>
      <ul class="contact">
        <li class="contact__item">
          <svg class="contact__icon" viewBox="0 0 18 14" aria-hidden="true"><rect x="1" y="1" width="16" height="12" fill="none" stroke="#444" stroke-width="1.2"/><path d="M1 1 L9 8 L17 1" fill="none" stroke="#444" stroke-width="1.2"/></svg>
          info@qmactive.com
        </li>
        <li class="contact__item">
          <svg class="contact__icon" viewBox="0 0 18 14" aria-hidden="true"><path d="M2 9 C2 3 16 3 16 9 L12 10 L12 7 C10 6 8 6 6 7 L6 10 Z" fill="none" stroke="#444" stroke-width="1.2" stroke-linejoin="round"/></svg>
          +65 5550 4172
        </li>
      </ul>
    </div>
    <div class="divider" aria-hidden="true"></div>
    <div class="brand-mark brand-mark--front">QM</div>
  </section>

  <section class="card card--back" aria-label="Business card back">
    <div class="pattern-field" role="img" aria-label="Full multicolour zigzag chevron pattern"></div>
    <div class="brand-mark brand-mark--back">QM</div>
  </section>
</main>
</body>
</html>
```